Business Card Design for a technology company

Our current business card is outdated and stale.

We need a new look and one soon.

We're a telematics (GPS tracking) company based in Australia. Our audiences are transport and logistics company.

Target Market(s)

1. Transport and Logistics Companies
2. Food and Beverage Manufacturers
3. Concrete Businesses

Industry/Entity Type

Logistics

Contact Information for Business Card

Halvor Pinet

Font styles to use
Sans Serif

Colors
3276b5
0255a3
85acd3
cfdeed
ffffff

Requirements
Must have
• Logo
• "Premium Suppliers of Real Time Temperature Tracking"
• Contact Name
• Business Title
• Address
• Telephone
• Mobile
• Email
• Website URL
Nice to have
• Visual representation of tracking or maps.
Should not have
• Image of a satellite as currently shown

```html
<!DOCTYPE html>
<html lang="en">
<head>
<meta charset="utf-8">
<title>Halvor Pinet – Business Card</title>
<link rel="stylesheet" href="https://fonts.googleapis.com/css2?family=Arimo:ital,wght@0,400;0,700;1,400;1,700&display=swap">
<style>
  :root {
    --page: #e9ecef;
    --card-light: #e7e8ea;
    --brand-blue: #0255a3;
    --ink-dark: #2b2f36;
    --night: #0b1420;
    --night-blue: #123550;
    --deep-blue: #163f63;
    --mid-blue: #3276b5;
    --pale-blue: #85acd3;
    --sky-blue: #1f9ad8;
    --white: #ffffff;
  }
  * { margin: 0; padding: 0; box-sizing: border-box; }
  html, body { width: 1200px; height: 900px; overflow: hidden; }
  body {
    background: var(--page);
    font-family: "Arimo", Arial, sans-serif;
    position: relative;
  }
  .card {
    position: absolute;
    width: 591px;
    height: 346px;
    overflow: hidden;
    box-shadow: 0 4px 14px rgba(0,0,0,.25);
  }
  .card--front { left: 274px; top: 94px; background: var(--night); }
  .card--back { left: 359px; top: 467px; background: var(--card-light); }

  /* front */
  .front-art { position: absolute; inset: 0; }
  .brand {
    position: absolute;
    display: flex;
    align-items: center;
    gap: 8px;
    color: var(--brand-blue);
    font-weight: 700;
    white-space: nowrap;
  }
  .brand__dot {
    border-radius: 50%;
    background: var(--brand-blue);
    flex: none;
  }
  .card--front .brand { left: 58px; top: 50px; font-size: 31px; }
  .card--front .brand__dot { width: 14px; height: 14px; }
  .tagline {
    position: absolute;
    font-style: italic;
    color: var(--ink-dark);
    font-size: 12px;
  }
  .card--front .tagline { left: 168px; top: 88px; }
  .front-slogan {
    position: absolute;
    left: 38px; top: 110px;
    font-style: italic;
    font-size: 15.5px;
    color: var(--ink-dark);
  }
  .contact {
    position: absolute;
    left: 36px; top: 164px;
    color: var(--white);
  }
  .contact__name { font-size: 23px; font-weight: 700; line-height: 1.1; }
  .contact__title { font-size: 12px; color: var(--pale-blue); margin-top: 3px; }
  .contact__mobile { font-size: 13px; font-weight: 700; margin-top: 3px; }
  .contact__details { font-size: 14px; line-height: 18px; margin-top: 12px; }

  /* back */
  .back-photo { position: absolute; left: 0; top: 148px; width: 591px; height: 157px; }
  .card--back .brand { left: 0; right: 0; top: 62px; justify-content: center; font-size: 40px; }
  .card--back .brand__dot { width: 16px; height: 16px; }
  .card--back .tagline { left: 286px; top: 118px; font-size: 14px; }
  .back-premium {
    position: absolute; left: 0; right: 0; top: 164px;
    text-align: center; color: var(--pale-blue);
    font-size: 13px; font-weight: 700; letter-spacing: .3px;
  }
  .back-phone {
    position: absolute; left: 0; right: 0; top: 188px;
    text-align: center; color: var(--white);
    font-size: 28px; font-weight: 700;
  }
  .back-quote {
    position: absolute; left: 0; right: 0; top: 232px;
    text-align: center; color: var(--white);
    font-style: italic; font-size: 19px; line-height: 25px;
  }
  .back-band {
    position: absolute; left: 0; top: 305px; width: 591px; height: 41px;
    background: var(--sky-blue);
    color: var(--white);
    font-size: 17px; font-weight: 700;
    display: flex; align-items: center; justify-content: center;
  }
</style>
</head>
<body>
  <section class="card card--front">
    <svg class="front-art" width="591" height="346" viewBox="0 0 591 346">
      <defs>
        <linearGradient id="road" x1="0" y1="0" x2="1" y2="1">
          <stop offset="0" stop-color="#3a5466"/>
          <stop offset="1" stop-color="#10263a"/>
        </linearGradient>
        <linearGradient id="panel" x1="0" y1="0" x2="1" y2="0">
          <stop offset="0" stop-color="#0b1420"/>
          <stop offset="1" stop-color="#16324c"/>
        </linearGradient>
        <linearGradient id="network" x1="0" y1="0" x2="1" y2="0">
          <stop offset="0" stop-color="#1d4a6e" stop-opacity="0"/>
          <stop offset="1" stop-color="#1d4a6e"/>
        </linearGradient>
      </defs>
      <rect width="591" height="346" fill="url(#panel)"/>
      <rect x="260" y="0" width="331" height="143" fill="url(#road)" role="img" aria-label="Photo of trucks and cars on a highway with a location pin"/>
      <rect x="380" y="143" width="211" height="203" fill="url(#network)" role="img" aria-label="Glowing network nodes joined by dotted lines"/>
      <polygon points="0,0 266,0 366,143 0,143" fill="var(--card-light)"/>
    </svg>
    <div class="brand"><span class="brand__dot"></span>Halvor Pinet</div>
    <div class="tagline">Your eye in the sky</div>
    <div class="front-slogan">Watch and Monitor on the Web 24/7</div>
    <div class="contact">
      <div class="contact__name">Lena Corrowe</div>
      <div class="contact__title">Business Development Manager</div>
      <div class="contact__mobile">M: 0400 555 318</div>
      <div class="contact__details">
        Pinet Track Rentals Pty Ltd ABN: 42 608 317 594<br>
        4, 18 Marlow Street, Kelso VIC 3190<br>
        T:+61 3 9555 0142 F: +61 3 9555 0143<br>
        lcorrowe@pinettrack.com.au<br>
        www.pinettrack.com.au
      </div>
    </div>
  </section>

  <section class="card card--back">
    <svg class="back-photo" width="591" height="157" viewBox="0 0 591 157" role="img" aria-label="Blue-tinted photo of parked trucks">
      <defs>
        <linearGradient id="trucks" x1="0" y1="0" x2="1" y2="1">
          <stop offset="0" stop-color="#1d4a70"/>
          <stop offset="1" stop-color="#12324f"/>
        </linearGradient>
      </defs>
      <rect width="591" height="157" fill="url(#trucks)"/>
    </svg>
    <div class="brand"><span class="brand__dot"></span>Halvor Pinet</div>
    <div class="tagline">Your eye in the sky</div>
    <div class="back-premium">PREMIUM SUPPLIERS OF REAL TIME TEMPERATURE TRACKING</div>
    <div class="back-phone">PH 1800 555 274</div>
    <div class="back-quote">“Our commitment through understanding will<br>allow as to achieve the desired result.”</div>
    <div class="back-band">WATCH AND MONITOR ON THE WEB 24/7</div>
  </section>
</body>
</html>
```